Marwick Agency (http://mk.fennoweb-studio.com/)

We are looking for a similar design to what we have, but more professional looking and cleaned up with links and logo that is not so grainy looking. We are an independent insurance agency marketing to personal and commercial clients. We offer all commercial lines markets and all personal lines. We target excavators, landscapers, restaurants, golf courses, contractors. Please look at http://mk.fennoweb-studio.com/ which we had designed but do not like it, it will give you an idea of what we are looking for.

Target Market(s)

Commercial and personal insurance. All business products and all personal (homeowners, auto, antique auto, umbrella)

Industry/Entity Type

It Professional

Logo Text

Knowledge Building Your Assurance

Number of Pages Required

5+ page

Colors
000000
848484
0255a3

```html
<!DOCTYPE html>
<html lang="en">
<head>
<meta charset="utf-8">
<title>Marwick Agency</title>
<link href="https://fonts.googleapis.com/css2?family=Open+Sans:wght@300;400;600;700&display=swap" rel="stylesheet">
<style>
  :root {
    --black: #000000;
    --grey: #848484;
    --blue: #0255a3;
    --nav-blue: #2f8fe0;
    --white: #ffffff;
    --text-dark: #222222;
    --rule: #dddddd;
    --fairway-top: #a9bb8c;
    --fairway-mid: #6a8d3a;
    --fairway-low: #3f6b1d;
  }
  * { margin: 0; padding: 0; box-sizing: border-box; }
  html, body { width: 761px; height: 1200px; overflow: hidden; background: var(--white); }
  body { font-family: 'Open Sans', Arial, sans-serif; position: relative; }

  .site-header { position: absolute; left: 0; top: 0; width: 761px; height: 84px; background: var(--black); }
  .brand { position: absolute; left: 34px; top: 12px; color: var(--white); font-size: 30px; font-weight: 700; letter-spacing: -0.5px; line-height: 36px; }
  .call-button { position: absolute; left: 341px; top: 22px; width: 245px; height: 27px; background: var(--blue); border-radius: 3px; color: var(--white); font-size: 15px; font-weight: 600; line-height: 27px; text-align: center; }
  .social { position: absolute; left: 667px; top: 27px; display: flex; gap: 7px; }
  .social span { width: 17px; height: 17px; border-radius: 50%; display: block; }
  .social .s1 { background: #1f5fa8; }
  .social .s2, .social .s3 { background: #777777; }

  .main-nav { position: absolute; left: 34px; top: 63px; display: flex; align-items: center; font-size: 9px; font-weight: 600; color: var(--white); text-transform: uppercase; white-space: nowrap; }
  .main-nav a { color: inherit; text-decoration: none; }
  .main-nav a.active { color: var(--nav-blue); font-weight: 400; }
  .main-nav .sep { margin: 0 11px; }

  .hero { position: absolute; left: 5px; top: 84px; width: 752px; height: 311px; background: linear-gradient(180deg, var(--fairway-top) 0%, var(--fairway-mid) 45%, var(--fairway-low) 100%); overflow: hidden; }
  .hero-caption { position: absolute; left: 110px; top: 200px; width: 533px; height: 58px; background: rgba(255,255,255,0.35); font-size: 50px; font-weight: 300; color: #111111; line-height: 58px; text-align: center; letter-spacing: -0.5px; }
  .hero-arrow { position: absolute; top: 140px; }
  .hero-arrow.prev { left: 6px; }
  .hero-arrow.next { right: 6px; }
  .hero-dots { position: absolute; left: 358px; top: 290px; display: flex; gap: 5px; }
  .hero-dots span { width: 8px; height: 8px; border-radius: 50%; background: rgba(255,255,255,0.6); }
  .hero-dots span.on { background: var(--white); }

  .intro { position: absolute; left: 0; top: 408px; width: 761px; text-align: center; }
  .intro h1 { font-size: 20px; font-weight: 400; color: var(--blue); text-transform: uppercase; line-height: 26px; }
  .intro p { margin-top: 6px; font-size: 13px; color: var(--text-dark); }

  .service { position: absolute; width: 338px; text-align: center; }
  .service .photo { width: 338px; height: 193px; position: relative; }
  .service h2 { margin-top: 14px; font-size: 19px; font-weight: 400; color: var(--text-dark); text-transform: uppercase; line-height: 26px; }
  .service p { margin-top: 8px; font-size: 10.3px; font-weight: 300; color: var(--grey); line-height: 14.6px; text-align: justify; text-align-last: center; }
  .business { left: 35px; top: 474px; }
  .auto { left: 389px; top: 474px; }
  .life { left: 35px; top: 790px; }
  .home { left: 389px; top: 790px; }
  .business .photo { background: linear-gradient(180deg, #86aee3 0%, #c6d8ee 50%, #8c9a45 75%, #6f7f2e 100%); }
  .auto .photo { background: linear-gradient(180deg, #2e2e2e 0%, #6b5a52 45%, #8a7063 70%, #262626 100%); }
  .life .photo { background: linear-gradient(180deg, #4f8fd9 0%, #a3c6ec 45%, #6aa040 75%, #3f7d24 100%); }
  .home .photo { background: linear-gradient(180deg, #f3f3f3 0%, #e2d3b4 50%, #e9cdbb 80%, #f4f4f4 100%); }

  .quote-button { position: absolute; left: 113px; top: 83px; width: 112px; height: 30px; background: rgba(40,40,40,0.75); border-radius: 3px; color: var(--white); font-size: 10.5px; font-weight: 600; display: flex; align-items: center; justify-content: center; gap: 7px; }

  .footer-rule { position: absolute; left: 5px; top: 1126px; width: 752px; border-top: 1px solid var(--rule); }
  .footer-nav { position: absolute; left: 0; top: 1147px; width: 761px; display: flex; justify-content: center; font-size: 9px; color: var(--text-dark); text-transform: uppercase; white-space: nowrap; }
  .footer-nav a { color: inherit; text-decoration: none; }
  .footer-nav a.active { color: var(--blue); }
  .footer-nav .sep { margin: 0 11px; }
  .copyright { position: absolute; left: 0; top: 1174px; width: 761px; text-align: center; font-size: 8px; color: #555555; }
</style>
</head>
<body>
  <header class="site-header">
    <div class="brand">Marwick Agency</div>
    <div class="call-button">CALL US TODAY: 1-888-555-0142</div>
    <div class="social"><span class="s1"></span><span class="s2"></span><span class="s3"></span></div>
    <nav class="main-nav">
      <a class="active" href="#">Home</a><span class="sep">|</span>
      <a href="#">Personal Insurance</a><span class="sep">|</span>
      <a href="#">Business Insurance</a><span class="sep">|</span>
      <a href="#">Service Center</a><span class="sep">|</span>
      <a href="#">About Us</a><span class="sep">|</span>
      <a href="#">Contact Us</a>
    </nav>
  </header>

  <section class="hero" role="img" aria-label="Gloved hand placing a golf ball on a tee beside a golf club on a green fairway">
    <svg class="hero-arrow prev" width="16" height="26" viewBox="0 0 16 26"><polyline points="13,2 3,13 13,24" fill="none" stroke="rgba(255,255,255,0.75)" stroke-width="3"/></svg>
    <svg class="hero-arrow next" width="16" height="26" viewBox="0 0 16 26"><polyline points="3,2 13,13 3,24" fill="none" stroke="rgba(255,255,255,0.75)" stroke-width="3"/></svg>
    <div class="hero-caption">Golf Course Insurance</div>
    <div class="hero-dots"><span class="on"></span><span></span><span></span></div>
  </section>

  <section class="intro">
    <h1>Small enough to care, big enough to make a difference</h1>
    <p>Please find information about our agency, its principles, and the various types of insurance coverages that we provide.</p>
  </section>

  <article class="service business">
    <div class="photo" role="img" aria-label="Two businessmen under a red umbrella standing in a grassy field">
      <div class="quote-button">
        <svg width="16" height="16" viewBox="0 0 16 16"><path d="M3 1h7l3 3v11H3z" fill="none" stroke="#ffffff" stroke-width="1.4"/><line x1="5" y1="11" x2="12" y2="4" stroke="#ffffff" stroke-width="1.6"/></svg>
        GET A QUOTE
      </div>
    </div>
    <h2>Business Insurance</h2>
    <p>Lorem Ipsum is simply dummy text of the printing and typesetting industry. Lorem Ipsum has been the industry's standard dummy text ever since the 1500s, when an unknown printer took a galley of type and scrambled it to make a type specimen book.</p>
  </article>

  <article class="service auto">
    <div class="photo" role="img" aria-label="Cupped hands holding a small blue toy convertible car"></div>
    <h2>Auto Insurance</h2>
    <p>Lorem Ipsum is simply dummy text of the printing and typesetting industry. Lorem Ipsum has been the industry's standard dummy text ever since the 1500s, when an unknown printer took a galley of type and scrambled it to make a type specimen book.</p>
  </article>

  <article class="service life">
    <div class="photo" role="img" aria-label="Family with two children walking hand in hand on a lawn under a blue sky"></div>
    <h2>Life Insurance</h2>
    <p>Lorem Ipsum is simply dummy text of the printing and typesetting industry. Lorem Ipsum has been the industry's standard dummy text ever since the 1500s, when an unknown printer took a galley of type and scrambled it to make a type specimen book.</p>
  </article>

  <article class="service home">
    <div class="photo" role="img" aria-label="Open hands holding a small model house"></div>
    <h2>Home Insurance</h2>
    <p>Lorem Ipsum is simply dummy text of the printing and typesetting industry. Lorem Ipsum has been the industry's standard dummy text ever since the 1500s, when an unknown printer took a galley of type and scrambled it to make a type specimen book.</p>
  </article>

  <footer>
    <div class="footer-rule"></div>
    <nav class="footer-nav">
      <a class="active" href="#">Home</a><span class="sep">|</span>
      <a href="#">Personal Insurance</a><span class="sep">|</span>
      <a href="#">Business Insurance</a><span class="sep">|</span>
      <a href="#">Service Center</a><span class="sep">|</span>
      <a href="#">About Us</a><span class="sep">|</span>
      <a href="#">Contact Us</a>
    </nav>
    <p class="copyright">© 2015 marwick agency, All rights reserved.</p>
  </footer>
</body>
</html>
```